I need a creative wine label design for my brand called ZAP ZEE. A design that catches the eye of the millennial consumer! Something very creative and playing off of the ZAP ZEE concept.

This will be a Red Blend 2019 vintage from California

Target Market(s)

Millennial wine consumer

Requirements
Must have
• Must have a design that attracts the millennial wine consumer. This must have creative flare.
Should not have
• Nothing corny!

```html
<!DOCTYPE html>
<html lang="en">
<head>
<meta charset="utf-8">
<title>ZAP ZEE Red Blend 2019 – Wine Label</title>
<link rel="stylesheet" href="https://fonts.googleapis.com/css2?family=Playfair+Display:wght@700;900&family=Montserrat:wght@500;600&display=swap">
<style>
  :root {
    --page: #f6f6f6;
    --panel: rgba(26, 22, 26, 0.93);
    --blue: #1a9bd6;
    --teal: #2aa7c9;
    --magenta: #c22a8c;
    --orange: #f08a1c;
    --deep-orange: #e6501a;
    --yellow: #f6d20c;
    --lime: #d8e010;
    --crimson: #d8284e;
    --gold: #f7c41a;
    --white: #ffffff;
    --rule-top: #c23393;
    --rule-bottom: #f1b21c;
  }
  * { margin: 0; padding: 0; box-sizing: border-box; }
  html, body {
    width: 1200px; height: 901px; overflow: hidden;
    background: var(--page);
  }
  .canvas { position: relative; width: 1200px; height: 901px; }
  .label {
    position: absolute; left: 292px; top: 40px;
    width: 615px; height: 820px;
    overflow: hidden;
  }
  .label-artwork {
    position: absolute; inset: 0;
    background:
      radial-gradient(ellipse 40% 12% at 20% 15%, var(--blue) 0%, transparent 80%),
      radial-gradient(ellipse 45% 10% at 45% 22%, var(--magenta) 0%, transparent 80%),
      radial-gradient(ellipse 30% 8% at 85% 12%, var(--yellow) 0%, transparent 80%),
      radial-gradient(ellipse 25% 10% at 8% 40%, var(--blue) 0%, transparent 80%),
      radial-gradient(ellipse 20% 8% at 10% 62%, var(--yellow) 0%, transparent 80%),
      radial-gradient(ellipse 25% 8% at 8% 72%, var(--teal) 0%, transparent 80%),
      radial-gradient(ellipse 30% 12% at 92% 70%, var(--crimson) 0%, transparent 80%),
      radial-gradient(ellipse 35% 10% at 50% 88%, var(--magenta) 0%, transparent 80%),
      radial-gradient(ellipse 25% 12% at 5% 95%, var(--lime) 0%, transparent 80%),
      radial-gradient(ellipse 35% 15% at 90% 92%, var(--deep-orange) 0%, transparent 80%),
      radial-gradient(ellipse 30% 30% at 92% 40%, var(--orange) 0%, transparent 80%),
      linear-gradient(160deg, var(--blue) 0%, var(--magenta) 30%, var(--orange) 55%, var(--crimson) 75%, var(--orange) 100%);
  }
  .label-panel {
    position: absolute; left: 101px; top: 135px;
    width: 412px; height: 549px;
    background: var(--panel);
    text-align: center;
  }
  .brand-name {
    position: absolute; left: 0; right: 0; top: 150px;
    font-family: "Playfair Display", Georgia, serif;
    font-weight: 900; font-size: 78px; line-height: 1;
    color: var(--gold);
    letter-spacing: 1px;
  }
  .divider {
    position: absolute; left: 50%; transform: translateX(-50%);
    width: 130px; height: 6px; border-radius: 3px;
  }
  .divider-top { top: 268px; background: var(--rule-top); }
  .divider-bottom { top: 510px; background: var(--rule-bottom); }
  .brand-subtitle {
    position: absolute; left: 0; right: 0; top: 290px;
    font-family: "Playfair Display", Georgia, serif;
    font-weight: 700; font-size: 29px; line-height: 1.1; letter-spacing: 4px;
    color: var(--white);
  }
  .wine-type {
    position: absolute; left: 0; right: 0; top: 416px;
    font-family: "Montserrat", Arial, sans-serif;
    font-weight: 600; font-size: 16px; line-height: 1.1; letter-spacing: 2.5px;
    color: var(--white);
  }
  .vintage-year {
    position: absolute; left: 0; right: 0; top: 434px;
    font-family: "Playfair Display", Georgia, serif;
    font-weight: 700; font-size: 42px; line-height: 1.1;
    color: var(--white);
  }
  .vintage-word {
    position: absolute; left: 0; right: 0; top: 480px;
    font-family: "Montserrat", Arial, sans-serif;
    font-weight: 500; font-size: 16px; line-height: 1.1; letter-spacing: 3px;
    color: var(--white);
  }
</style>
</head>
<body>
<main class="canvas">
  <section class="label">
    <div class="label-artwork" role="img" aria-label="Fluid marbled swirls of blue, magenta, orange, yellow and red"></div>
    <div class="label-panel">
      <h1 class="brand-name">ZAP ZEE</h1>
      <div class="divider divider-top" role="img" aria-label="Magenta and yellow zigzag ornament"></div>
      <p class="brand-subtitle">ZAP ZEE</p>
      <p class="wine-type">RED BLEND</p>
      <p class="vintage-year">2019</p>
      <p class="vintage-word">VINTAGE</p>
      <div class="divider divider-bottom" role="img" aria-label="Blue and yellow zigzag ornament"></div>
    </div>
  </section>
</main>
</body>
</html>
```